PulseRoute Tri-Fold Design & Box Layout

Need Tri-Fold Design for new brand called PulseRoute Mobile. The design should be based on colors, logo, and text copy on www.pulseroutemobile-example.com See uploads for templates to use and ask questions. I am very responsive. Also need artwork for mobile phone box to go with the flyer design concept. The box can be very generic but same color theme, etc. with logo.

Target Market(s)

all types of people but focused on the sub-prime market.

Industry/Entity Type

Wireless Communication

Font styles to use
Serif
Sans Serif

Colors
33a6d7
abd036
f78f20

Requirements
Must have
• tri-fold and box layout using provided templates. do not outline any text as we may want to update before going to print. See layout for Tri-Fold as some will be English and some Spanish. Its OK if you just duplicate the English and we will translate as needed.
Nice to have
• Colors in Logo are:
• Green - #C5D42D
• Orange - #F6941F
• Blue - #58BAE9
Should not have
• no images of people.

```html
<!DOCTYPE html>
<html lang="en">
<head>
<meta charset="utf-8">
<title>PulseRoute Mobile Tri-Fold</title>
<link href="https://fonts.googleapis.com/css2?family=Didact+Gothic&family=Montserrat:wght@600;700&display=swap" rel="stylesheet">
<style>
:root{
  --bg:#e9eaec;
  --green:#7fb72d;
  --lime:#b5d133;
  --lime-deep:#9cc42a;
  --blue-head:#1c6fb5;
  --sky:#6cc0ee;
  --sky-light:#bfe3f8;
  --ink:#4a4a4a;
  --white:#ffffff;
  --orange:#f78f20;
}
*{box-sizing:border-box;margin:0;padding:0}
html,body{width:1164px;height:1200px;overflow:hidden;background:var(--bg)}
body{font-family:"Didact Gothic",sans-serif;color:var(--ink);position:relative}
.trifold{position:absolute;left:24px;top:337px;width:1116px;height:525px;background:var(--white);box-shadow:0 4px 14px rgba(0,0,0,.25);overflow:hidden}
.panel{position:absolute;top:0;width:372px;height:525px}
.panel--why{left:0;background:var(--white)}
.panel--contact{left:372px;background:linear-gradient(180deg,var(--sky) 0%,#8ccef2 55%,var(--sky-light) 100%);color:var(--white);text-align:center}
.panel--cover{left:744px;overflow:hidden}
.heading{font-family:"Montserrat",sans-serif;font-weight:700;text-transform:uppercase;letter-spacing:.2px}
.why-title{position:absolute;top:30px;left:0;width:372px;text-align:center;color:var(--green);font-size:20px}
.reasons{position:absolute;top:75px;left:18px;width:340px}
.reason{display:flex;margin-bottom:10px}
.reason h3{width:126px;flex:none;font-family:"Montserrat",sans-serif;font-weight:600;font-size:11.5px;line-height:14px;color:var(--blue-head);text-transform:uppercase}
.reason p{font-size:8.6px;line-height:10.6px;text-align:justify}
.reason--tall h3{padding-top:14px}
.phone-photo{position:absolute;left:28px;top:304px;width:120px;height:221px;border-radius:22px 22px 0 0;background:linear-gradient(180deg,#6fa6d8 0%,#9dbb7a 45%,#a0623a 80%,#e8c9b0 100%)}
.lorem{position:absolute;left:170px;top:308px;width:192px;font-size:8.6px;line-height:10.6px;text-align:justify}
.lorem p{margin-bottom:12px}
.call{position:absolute;left:170px;top:452px;width:195px;text-align:center}
.call-label{font-size:24px;color:var(--green);letter-spacing:.5px;line-height:26px}
.call-number{font-family:"Montserrat",sans-serif;font-weight:700;font-size:27px;color:var(--blue-head);line-height:32px}
.contact-title{margin-top:30px;font-size:19.5px;color:var(--white)}
.contact-list{list-style:none;margin-top:22px}
.contact-list li{font-size:12.5px;line-height:14px;margin-bottom:17px}
.contact-list svg{display:block;margin:0 auto 3px}
.card{position:absolute;left:40px;top:310px;width:302px;height:180px;background:var(--white);border-radius:30px 0 30px 0;box-shadow:0 3px 8px rgba(0,0,0,.12)}
.brand{display:flex;align-items:center;justify-content:center;gap:7px;font-family:"Montserrat",sans-serif;font-weight:600;color:var(--blue-head)}
.brand-dot{width:12px;height:12px;border-radius:50%;background:var(--orange);flex:none}
.card .brand{margin-top:32px;font-size:20px}
.cover-photo{position:absolute;inset:0;background:linear-gradient(135deg,#6f7a4a 0%,#b58a5a 35%,#c9a98c 55%,#8aa0b8 80%,#6d8c6a 100%)}
.badge{position:absolute;left:3px;top:-98px;width:196px;height:196px;border-radius:50%;background:var(--white);display:flex;align-items:flex-end;justify-content:center;padding-bottom:44px}
.badge .brand{font-size:19px}
.cover-title{position:absolute;left:18px;top:130px;width:180px;color:var(--white);font-size:21px;line-height:25px;text-shadow:0 1px 3px rgba(0,0,0,.35)}
.sweep{position:absolute;left:0;top:0;width:1116px;height:525px;pointer-events:none}
.steps-intro{position:absolute;right:22px;top:395px;width:220px;text-align:center;color:#4d6a10;font-size:13.5px;line-height:17px;text-transform:uppercase}
.steps-label{position:absolute;left:772px;top:474px;color:#2f5d9a;font-family:"Montserrat",sans-serif;font-weight:600;font-size:12px;line-height:16px;text-transform:uppercase;width:104px}
.steps{position:absolute;left:880px;top:460px;display:flex;gap:2px;list-style:none}
.steps li{width:72px;text-align:center;font-size:8px;line-height:9.5px;color:#3b5a12;text-transform:uppercase;white-space:nowrap}
.step-icon{width:36px;height:36px;border-radius:50%;background:var(--lime-deep);border:2px solid rgba(255,255,255,.6);margin:0 auto 3px;display:flex;align-items:center;justify-content:center}
</style>
</head>
<body>
<main class="trifold">
  <section class="panel panel--why">
    <h2 class="heading why-title">Why Choose Us</h2>
    <div class="reasons">
      <div class="reason"><h3>Simple Instant Credit Approval</h3><p>With a 95+% approval rate, and an order which can be completed in under 5 minutes, PulseRoute gets you on track in a way other carriers can't.</p></div>
      <div class="reason"><h3>Stress Free Buying Options</h3><p>PulseRoute takes the stress out of phone buying. We don't require everything to be paid up front to get talking, texting, or streaming!</p></div>
      <div class="reason"><h3>Get Your First Month Free</h3><p>PulseRoute provides you with a gift card so your first month is FREE! Never settle for less, choose PulseRoute</p></div>
      <div class="reason reason--tall"><h3>Best Device Protection Available</h3><p>Ever get your brand new phone and drop it? Scratch it? Lose it? Not only do PulseRoute packages include headphones, car charger, and screen protector, they also include insurance at no additional cost. Need a little extra coverage? We have you covered with upgrade options at time of package selection.</p></div>
    </div>
    <div class="phone-photo" role="img" aria-label="Hand holding a smartphone showing a railway track landscape"></div>
    <div class="lorem">
      <p>Lorem ipsum dolor sit amet, consectetur adipiscing elit, sed do eiusmod tempor incididunt ut labore et dolore magna aliqua. Ut enim ad minim veniam, quis nostrud exercitation ullamco laboris nisi ut aliquip ex ea commodo consequat.</p>
      <p>Duis aute irure dolor in reprehenderit in voluptate velit esse cillum dolore eu fugiat nulla pariatur. Excepteur sint occaecat cupidatat non proident, sunt in culpa qui officia deserunt mollit anim id est laborum.</p>
    </div>
    <div class="call">
      <div class="call-label">CALL US TODAY</div>
      <div class="call-number">800-555-0142</div>
    </div>
  </section>

  <section class="panel panel--contact">
    <h2 class="heading contact-title">Get In Touch With Us!</h2>
    <ul class="contact-list">
      <li><svg width="10" height="12" viewBox="0 0 10 12"><path d="M5 0a4 4 0 0 0-4 4c0 3 4 8 4 8s4-5 4-8a4 4 0 0 0-4-4zm0 5.5A1.5 1.5 0 1 1 5 2.5a1.5 1.5 0 0 1 0 3z" fill="#fff"/></svg>45 Harbor Ave.<br>Coral Bay, FL 32900</li>
      <li><svg width="11" height="9" viewBox="0 0 11 9"><path d="M1 3c0-2 9-2 9 0v1H7V3H4v1H1zM2 5h7l1 4H1z" fill="#fff"/></svg>555-010-2030</li>
      <li><svg width="11" height="8" viewBox="0 0 11 8"><rect width="11" height="8" rx="1" fill="#fff"/><path d="M0.5 0.8l5 3.5 5-3.5" stroke="#7fc6ef" fill="none"/></svg>info@pulseroutemobile-example.com</li>
      <li><svg width="10" height="10" viewBox="0 0 10 10"><circle cx="5" cy="5" r="4.3" fill="none" stroke="#fff" stroke-width="1.2"/><path d="M0.7 5h8.6M5 0.7c-2.5 2.5-2.5 6.1 0 8.6M5 0.7c2.5 2.5 2.5 6.1 0 8.6" stroke="#fff" fill="none"/></svg>www.pulseroutemobile-example.com</li>
    </ul>
    <div class="card"><div class="brand"><span class="brand-dot"></span>PulseRoute Mobile</div></div>
  </section>

  <section class="panel panel--cover">
    <div class="cover-photo" role="img" aria-label="Cover photograph of a customer talking on a mobile phone in a bright cafe"></div>
    <div class="badge"><div class="brand"><span class="brand-dot"></span>PulseRoute</div></div>
    <h1 class="heading cover-title">Welcome to the new age of wireless service!</h1>
  </section>

  <svg class="sweep" viewBox="0 0 1116 525" aria-hidden="true">
    <polygon points="640,525 1116,525 1116,408 1040,338 870,420" fill="#9cc42a" opacity=".55"/>
    <polygon points="660,525 1116,525 1116,418 1055,355 890,432" fill="#b5d133"/>
  </svg>
  <p class="steps-intro">Lorem ipsum dolor<br>sit amet, consectetur<br>adipiscing elit</p>
  <p class="steps-label">Three simple steps to your new phone</p>
  <ul class="steps">
    <li><div class="step-icon"><svg width="12" height="18" viewBox="0 0 12 18"><rect x="1" y="1" width="10" height="16" rx="2" fill="none" stroke="#fff" stroke-width="1.6"/><circle cx="6" cy="14" r="1" fill="#fff"/></svg></div>Choose<br>phone &amp; plan</li>
    <li><div class="step-icon"><svg width="16" height="14" viewBox="0 0 16 14"><path d="M2 7l4 4 8-9" fill="none" stroke="#fff" stroke-width="2.4"/></svg></div>Get<br>financing</li>
    <li><div class="step-icon"><svg width="16" height="16" viewBox="0 0 16 16"><path d="M1 7h3v8H1zM5 7l3-6c2 0 2 2 1.5 4H14c1 0 1.6 1 1.3 2l-1.5 6c-.3 1-1 2-2 2H5z" fill="#fff"/></svg></div>Receive your<br>phone in 3 days</li>
  </ul>
</main>
</body>
</html>
```